Stationery Design Project

Require letterhead/stationery design based on new logo (see attached).

Would prefer it kept simple but strong and effective.

Target Market(s)

Clients and building developers. Residential/consumer and corporate clientele.

```html
<!DOCTYPE html>
<html lang="en">
<head>
<meta charset="utf-8">
<title>Corvane Builds — Stationery Set</title>
<link rel="stylesheet" href="https://fonts.googleapis.com/css2?family=PT+Sans:wght@400;700&display=swap">
<style>
  :root {
    --stage-blue: #35bfee;
    --brand-blue: #2fb3e6;
    --paper: #ffffff;
    --ink: #3a3a3c;
    --ink-soft: #6d6e70;
    --card-black: #1d1d1f;
    --window-edge: #222222;
    --shadow: 0 3px 8px rgba(0, 60, 90, 0.28);
  }
  * { box-sizing: border-box; margin: 0; padding: 0; }
  html, body { width: 1200px; height: 848px; overflow: hidden; }
  body {
    background: var(--stage-blue);
    font-family: "PT Sans", sans-serif;
    color: var(--ink);
    position: relative;
  }
  .sheet, .card, .envelope {
    position: absolute;
    background: var(--paper);
    box-shadow: var(--shadow);
  }

  /* brand name lockup */
  .brand { display: flex; flex-direction: column; align-items: center; position: absolute; }
  .brand__mark { width: 22px; height: 22px; background: var(--brand-blue); margin-bottom: 5px; }
  .brand__name {
    font-size: 12px; font-weight: 700; letter-spacing: 1px;
    color: var(--ink-soft); text-transform: uppercase; white-space: nowrap;
  }
  .brand--small .brand__mark { width: 13px; height: 13px; margin-bottom: 3px; }
  .brand--small .brand__name { font-size: 6px; letter-spacing: 0.4px; }

  .link { color: var(--brand-blue); }
  .tiny { font-size: 7px; line-height: 1.4; position: absolute; white-space: nowrap; }

  /* letterheads */
  .letterhead { top: 64px; width: 357px; height: 503px; }
  .letterhead--left { left: 239px; }
  .letterhead--right { left: 640px; }
  .letterhead--left .brand { left: 42px; top: 24px; }
  .letterhead--right .brand { right: 40px; top: 24px; }
  .letterhead__web { top: 46px; right: 40px; }
  .letterhead__contact { bottom: 38px; right: 40px; text-align: right; }
  .letterhead__contact-left { bottom: 38px; left: 150px; }
  .letterhead__address { bottom: 20px; right: 40px; color: var(--ink); }

  /* business cards */
  .card { left: 131px; width: 150px; height: 88px; }
  .card--front { top: 606px; }
  .card--back { top: 707px; background: var(--card-black); color: #cfcfcf; }
  .card--front .brand { left: 12px; top: 9px; }
  .card--back .brand { right: 12px; top: 10px; }
  .card--back .brand__name { color: var(--ink-soft); }
  .card .tiny { font-size: 4.5px; }
  .card__slogan { left: 14px; top: 51px; font-size: 5px !important; }
  .card__details { left: 14px; top: 59px; }
  .card__back-slogan { left: 11px; top: 28px; }
  .card__back-address { right: 12px; top: 54px; text-align: right; }
  .card__back-web { left: 12px; bottom: 9px; }

  /* window envelope */
  .envelope { top: 607px; height: 187px; }
  .envelope--window { left: 318px; width: 373px; }
  .envelope--window .brand { left: 50px; top: 18px; }
  .envelope__window {
    position: absolute; left: 23px; top: 94px; width: 144px; height: 50px;
    background: var(--stage-blue); border: 1.5px solid var(--window-edge); border-radius: 7px;
  }
  .envelope__address { left: 181px; top: 23px; font-size: 7px; font-weight: 700; color: var(--ink); line-height: 1.45; white-space: normal; width: 150px; }
  .envelope__contact { left: 181px; top: 53px; }
  .envelope__web { left: 253px; top: 53px; }

  /* envelope back */
  .envelope--back { left: 728px; width: 376px; overflow: hidden; }
  .envelope__flap { position: absolute; left: 0; top: 0; }
  .envelope--back .brand { left: 50%; transform: translateX(-50%); top: 90px; }
</style>
</head>
<body>

<section class="sheet letterhead letterhead--left">
  <div class="brand"><span class="brand__mark"></span><span class="brand__name">Corvane Builds</span></div>
  <p class="tiny link letterhead__web">www.yourwebsite.com</p>
  <p class="tiny link letterhead__contact">+1 234 567 89 00<br>info@emailaddress.com</p>
  <p class="tiny letterhead__address">physical address and location related information here</p>
</section>

<section class="sheet letterhead letterhead--right">
  <div class="brand"><span class="brand__mark"></span><span class="brand__name">Corvane Builds</span></div>
  <p class="tiny link letterhead__contact-left">www.yourwebsite.com<br>info@emailaddress.com</p>
  <p class="tiny link letterhead__contact">+1 234 567 89 00<br>info@emailaddress.com</p>
  <p class="tiny letterhead__address">physical address and location related information here</p>
</section>

<section class="card card--front">
  <div class="brand brand--small"><span class="brand__mark"></span><span class="brand__name">Corvane Builds</span></div>
  <p class="tiny card__slogan">Your company slogan goes here</p>
  <p class="tiny card__details">Jordan Hale<br>Site Manager<br>+1 234 567 8900<br>info@emailaddress.com</p>
</section>

<section class="card card--back">
  <p class="tiny card__back-slogan">Your company slogan goes here</p>
  <div class="brand brand--small"><span class="brand__mark"></span><span class="brand__name">Corvane Builds</span></div>
  <p class="tiny card__back-address">Your address and location details here</p>
  <p class="tiny card__back-web">www.yourwebsite.com</p>
</section>

<section class="envelope envelope--window">
  <div class="brand"><span class="brand__mark"></span><span class="brand__name">Corvane Builds</span></div>
  <p class="tiny envelope__address">Your physical address and location related information goes here</p>
  <p class="tiny envelope__contact">+1 234 567 89 00<br>info@emailaddress.com</p>
  <p class="tiny link envelope__web">www.companywebsite.com</p>
  <div class="envelope__window"></div>
</section>

<section class="envelope envelope--back">
  <svg class="envelope__flap" width="376" height="60" viewBox="0 0 376 60" aria-hidden="true">
    <path d="M0 0 H376 V10 Q200 58 0 22 Z" fill="var(--stage-blue)"/>
  </svg>
  <div class="brand"><span class="brand__mark"></span><span class="brand__name">Corvane Builds</span></div>
</section>

</body>
</html>
```